Pipe and Drape Company Web site

Name of client is "Harbor Linen" with a tagline of, "The Finest Linen, The Finest Care." which will need to go across the middle of the header area. Logo will be on the left. Connectors on the right. Connectors being, join newsletter, framebook, chirpster, worked Up, etc...

Please refer to www.velvetmonarchs.example for feel and layout and then www.northfieldhawks.example for background imagery style and preferred color scheme. Colors for the site should be black and dark purple with sub page text areas being white with black text. Yet still surrounded with black framing and purple infused background. We'll need a Large impactful main image area to display scrolling images. Below that will be 4 content area boxes with each of the following titles. "Corporate Events" , "Weddings" , "Special Events" , and "Products".

Main nav will need to be across the top of main image and include the 5 following tabs: "Harbor Experience", "DrapeRental" , "Gallery" , "Resources" ,
"Contact Us". Also leave a blank space on the right end of main nav in case we decide to add a 6th main nav at a later date.

This is a nationwide company and is a leader in their industry. The site should look very high end and classy. Highest quality and largest selection of drape anywhere. It should convey dependability, professionalism, Trustworthy, and expertise.

The main calls to action should be to get the visitor to call the phone number, or contact via email.

Main visitor demographic will be female event coordinators.

Sub Page design will vary based on the market segment chosen from home page. However, we feel the "wedding" category would be a good option since those pages might have a lighter look and feminine feel to them. Be sure to make it simple for the visitor to go back from the sub page, to the hame page via nav choices, or market segment boxes across the bottom again.

```html
<!DOCTYPE html>
<html lang="en">
<head>
<meta charset="utf-8">
<title>Harbor Linen – Weddings</title>
<link rel="stylesheet" href="https://fonts.googleapis.com/css2?family=Arimo:wght@400;700&family=Open+Sans:ital,wght@0,400;1,400&display=swap">
<style>
:root{
  --plum-deep:#1d1229;
  --plum:#3b2e4f;
  --plum-glow:#7a4a78;
  --ink:#111;
  --frame:#0a0a0c;
  --paper:#fff;
  --line:#b9b9bf;
  --muted:#555;
  --bar-top:#3c3a44;
  --bar-bot:#050507;
}
*{box-sizing:border-box;margin:0;padding:0}
html,body{width:1200px;height:967px;overflow:hidden}
body{
  font-family:"Arimo",Arial,sans-serif;color:var(--ink);position:relative;
  background:
    radial-gradient(circle at 65px 140px,rgba(255,230,240,.55) 0,rgba(200,120,150,.25) 60px,transparent 160px),
    radial-gradient(circle at 1170px 230px,rgba(190,120,170,.35) 0,transparent 140px),
    linear-gradient(180deg,#2a1a33 0%,#3a2240 45%,#1f1428 70%,var(--plum-deep) 100%);
}
.page{position:absolute;left:120px;top:8px;width:958px;height:952px;background:var(--paper);border:1px solid var(--frame);border-radius:8px;overflow:hidden}
.abs{position:absolute}
/* header */
.brand{left:20px;top:22px;font-size:42px;font-weight:700;color:var(--plum);letter-spacing:-.5px}
.tagline{left:297px;top:28px;width:316px;height:36px;border-top:1px solid #999;border-bottom:1px solid #999;font-family:"Open Sans",sans-serif;font-style:italic;font-size:21px;line-height:34px;text-align:center;color:#111}
.connectors{left:726px;top:10px;width:224px;display:flex;justify-content:space-between}
.connectors span{font-size:10px;color:var(--plum);line-height:30px}
.newsletter{left:726px;top:47px;display:flex;align-items:center;gap:6px;font-family:"Open Sans",sans-serif;font-size:16px}
.email{left:726px;top:74px;width:166px;height:23px;border:1px solid #aaa;font-size:9px;color:#777;padding:5px 7px}
.btn{background:linear-gradient(var(--bar-top),var(--bar-bot));color:#fff;font-size:11px;font-weight:700;border-radius:4px;text-align:center}
.join{left:897px;top:72px;width:51px;height:25px;line-height:25px}
/* nav */
.nav{left:0;top:102px;width:958px;height:38px;background:linear-gradient(#4a4852,#15141a 50%,var(--bar-bot));display:flex;box-shadow:0 3px 4px rgba(0,0,0,.25)}
.nav a{color:#fff;text-decoration:none;font-size:12px;line-height:38px;text-align:center;border-right:1px solid #555}
/* content */
.crumb{left:8px;top:163px;font-size:11px}
.crumb b{font-weight:400;color:var(--plum);margin-left:4px}
h1{left:9px;top:188px;font-size:21px;color:var(--plum);font-weight:700}
.copy{font-size:12.5px;line-height:16px}
.intro{left:9px;top:222px;width:930px}
.body{left:9px;top:266px;width:670px}
.lead{left:9px;top:376px;font-size:12.5px;font-weight:700}
.below{left:9px;top:408px;font-size:12.5px}
.photo{border-radius:10px;border:1px solid #444}
.hero{left:700px;top:243px;width:251px;height:185px;background:linear-gradient(#e9dfc9,#f3f3f0 55%,#2b3f8a 95%)}
.reel{left:4px;top:438px;width:948px;height:184px;border:1px solid var(--line);border-radius:5px;background:linear-gradient(#fff,#eee)}
.edge{top:0;width:30px;height:182px;background:linear-gradient(90deg,#d8d8d8,#fff 40%,#777)}
.arrow{top:75px;font-size:22px;font-weight:700}
.shot{top:13px;width:200px;height:154px}
/* segment boxes */
.seg{top:630px;width:225px;height:264px;border:1px solid #ddd;background:linear-gradient(#fff 50%,#e8e8e8);box-shadow:1px 2px 3px rgba(0,0,0,.2)}
.seg h2{height:34px;background:linear-gradient(#3a3a40,#000 50%);color:#fff;font-weight:400;font-size:17px;line-height:32px;text-align:center;border-bottom:3px solid #999}
.icon{left:50%;top:45px;width:97px;height:75px;margin-left:-48px;border:1px solid #ccc;border-radius:4px;box-shadow:1px 2px 3px rgba(0,0,0,.2)}
.list{top:127px;left:0;width:100%;font-size:11px;line-height:16px;list-style:none;text-align:center}
.list li::before{content:"";display:inline-block;border-left:5px solid #000;border-top:4px solid transparent;border-bottom:4px solid transparent;margin-right:5px}
.list.plain li::before{display:none}
.more{right:4px;top:230px;width:51px;height:25px;line-height:25px}
/* footer */
.footer{left:0;top:912px;width:958px;height:40px;background:linear-gradient(#2a2830,#000);border-top:2px solid #fff;outline:1px solid #000}
.footer small{left:18px;top:13px;font-size:11px;color:#fff}
.footer .connectors{left:712px;top:4px;width:236px}
.footer .connectors span{color:#fff}
</style>
</head>
<body>
<div class="page">
  <header>
    <div class="abs brand">Harbor Linen</div>
    <div class="abs tagline">The Finest Linen, The Finest Care.</div>
    <div class="abs connectors"><span>chirpster</span><span>framebook</span><span>worked Up</span><span>Murmur</span><span>Clipstream</span></div>
    <div class="abs newsletter">
      <svg width="20" height="16" viewBox="0 0 20 16"><rect x="1" y="1" width="18" height="14" fill="#d9c6ea" stroke="#6b4a8a"/><path d="M1 1l9 8 9-8" fill="none" stroke="#6b4a8a" stroke-width="1.5"/></svg>
      Join Newsletter
    </div>
    <div class="abs email">Enter Email Address</div>
    <div class="abs btn join">Join</div>
  </header>
  <nav class="abs nav">
    <a style="width:81px">HOME</a><a style="width:165px">HARBOR EXPERIENCE</a><a style="width:135px">DRAPE RENTAL</a><a style="width:98px">GALLERY</a><a style="width:123px">RESOURCES</a><a style="width:123px;border:0">CONTACT US</a>
  </nav>
  <main>
    <p class="abs crumb">You are here Home <span>»</span><b>Weddings</b></p>
    <h1 class="abs">WEDDINGS</h1>
    <p class="abs copy intro">Lorem ipsum dolor sit amet consecutor. Lorem ipsum dolor sit amet consecutor. Lorem ipsum dolor sit amet consecutor. Lorem ipsum dolor sit amet consecutor. Lorem ipsum dolor sit amet consecutor.Lorem ipsum dolor sit amet consecutor.</p>
    <p class="abs copy body">Lorem ipsum dolor sit amet consecutor. Lorem ipsum dolor sit amet consecutor. Lorem ipsum dolor sit amet consecutor. Lorem ipsum dolor sit amet consecutor. Lorem ipsum dolor sit amet consecutor.Lorem ipsum dolor sit amet consecutor. Lorem ipsum dolor sit amet consecutor. Lorem ipsum dolor sit amet consecutor. Lorem ipsum dolor sit amet consecutor. Lorem ipsum dolor sit amet consecutor. Lorem ipsum dolor sit amet consecutor.Lorem ipsum dolor sit amet consecutor. Lorem ipsum dolor sit amet consecutor. Lorem ipsum dolor sit amet consecutor. Lorem ipsum dolor sit amet consecutor. Lorem ipsum dolor sit amet consecutor. Lorem ipsum dolor sit amet consecutor.Lorem ipsum dolor sit amet consecutor.</p>
    <p class="abs lead">See Harbor Linen in Action</p>
    <p class="abs below">Below are a few photos from some of the weddings we have done:</p>
    <div class="abs photo hero" role="img" aria-label="Wedding ceremony tent with draped tables, flower arrangements and white chairs"></div>
    <section class="abs reel">
      <div class="abs edge" style="left:0"></div>
      <div class="abs edge" style="right:0;transform:scaleX(-1)"></div>
      <div class="abs arrow" style="left:6px">←</div>
      <div class="abs arrow" style="right:6px">→</div>
      <div class="abs photo shot" style="left:40px;background:linear-gradient(#bdb8b2,#3a3434)" role="img" aria-label="Wedding guests sharing cake with the bride and groom"></div>
      <div class="abs photo shot" style="left:259px;background:linear-gradient(#d6d0c8,#6b6058)" role="img" aria-label="Bride and groom celebrating with friends"></div>
      <div class="abs photo shot" style="left:480px;background:linear-gradient(#d3c4bc,#e9dfe2)" role="img" aria-label="Wedding cake topped with sugar flowers"></div>
      <div class="abs photo shot" style="left:704px;background:linear-gradient(#d8d2cc,#a89888)" role="img" aria-label="Groom feeding wedding cake to the bride"></div>
    </section>
    <section class="abs seg" style="left:4px">
      <h2>Corporate Events</h2>
      <div class="abs icon" style="background:linear-gradient(#fff,#e6e6e6)" role="img" aria-label="Calendar icon"></div>
      <ul class="abs list"><li>Lorem ipsum dolor Event</li><li>Lorem ipsum dolor Event</li><li>Lorem ipsum dolor Event</li><li>Lorem ipsum dolor Event</li><li>Lorem ipsum dolor Event</li><li>Lorem ipsum dolor Event</li></ul>
      <div class="abs btn more">more</div>
    </section>
    <section class="abs seg" style="left:245px">
      <h2>Weddings</h2>
      <div class="abs icon" style="background:linear-gradient(#fff,#f0e2c0)" role="img" aria-label="Gold wedding rings icon"></div>
      <ul class="abs list plain"><li>Lorem ipsum dolor sit amet consecutor.</li><li>Lorem ipsum dolor sit amet consecutor.</li><li>Lorem ipsum dolor sit amet consecutor.</li><li>Lorem ipsum dolor sit amet consecutor.</li><li>Lorem ipsum dolor sit amet consecutor.</li><li>Lorem ipsum dolor sit amet consecutor.</li></ul>
      <div class="abs btn more">more</div>
    </section>
    <section class="abs seg" style="left:486px">
      <h2>Special Events</h2>
      <div class="abs icon" style="background:linear-gradient(#fff,#dbe6f5)" role="img" aria-label="Birthday cake icon"></div>
      <ul class="abs list"><li>Lorem ipsum dolor Event</li><li>Lorem ipsum dolor Event</li><li>Lorem ipsum dolor Event</li><li>Lorem ipsum dolor Event</li><li>Lorem ipsum dolor Event</li><li>Lorem ipsum dolor Event</li></ul>
      <div class="abs btn more">more</div>
    </section>
    <section class="abs seg" style="left:727px">
      <h2>Products</h2>
      <div class="abs icon" style="background:linear-gradient(#fff,#ead8b8)" role="img" aria-label="Open product box icon"></div>
      <ul class="abs list"><li>Products 1</li><li>Products 2</li><li>Products 3</li><li>Products 4</li><li>Products 5</li><li>Products 6</li></ul>
      <div class="abs btn more">more</div>
    </section>
  </main>
  <footer class="abs footer">
    <small class="abs">© 2011 Harbor Linen, All Rights Reserved</small>
    <div class="abs connectors"><span>chirpster</span><span>framebook</span><span>worked Up</span><span>Murmur</span><span>Clipstream</span></div>
  </footer>
</div>
</body>
</html>
```